Mail - Scan, Sort & Forward - Web Design

We need a web design for a mail scan, store, view and forward service. It is a lifestyle service predicated on freedom, convenience, ease of access, ease of use, security, safety. It involves personal information and is accessed remotely.
No branding or style guide is yet complete so an open pallet is available but design should convey simplicity as it targets demographic 45-75 years travellers but also high net worth multi location professionals, miners and other multi-location workers.
Competitor sites are: (for business description examples)
www.quellarbox.example
www.trimbeldesk.example.au
www.norvandelsupply.example.au
Updates

Attached files are wireframes which show how the service will work (UI). You should use these to form ideas about your web design for the service. They are not templates nor am I looking for a UI dev (yet).

Target Market(s)

Travellers ( especially retirees) and multi-location workers eg miners

Industry/Entity Type

Business

Requirements
Must have
• Being a lifestyle site, the pages must be low on text, lite layout, imagery addressing the target market.
Navigation should be simple to use
Concept of visitor / member / client should be addressed. The user needs to be able to permission other user groups (read-only)
Talk to reasons why prospects want to use this service.
Nice to have
• access to view nearest Kelm Rout office.
Regular call to action like survey, quiz or did you know info which may keep the user returning to the site.
Campaign section which enables customising of campaigns on an ongoing basis
Ability to access and download Terms & conditions, brochures .pdf or other information.
Simulate how service works..video or webcast
Should not have
• Do not want heavy or dense text everywhere. Use imagery where possible. Icons should be thematic not isolated.

```html
<!DOCTYPE html>
<html lang="en">
<head>
<meta charset="utf-8">
<title>lettrova.example – Mail Scan, Sort &amp; Forward</title>
<link rel="stylesheet" href="https://fonts.googleapis.com/css2?family=Arimo:wght@400;700&display=swap">
<style>
:root{
  --blue:#1d5fad;
  --blue-deep:#0d4d9c;
  --blue-bar:#2a6fb0;
  --grey-text:#555a5f;
  --ink:#1b1b1b;
  --red:#cc0000;
  --line:#cfd4d9;
  --nav-dark:#151515;
  --sky-1:#ffffff;
  --sky-2:#dcebf4;
  --sky-3:#a9cde0;
  --white:#ffffff;
}
*{box-sizing:border-box;margin:0;padding:0}
html,body{width:1083px;height:1200px;overflow:hidden;background:var(--white)}
body{font-family:"Arimo",Arial,sans-serif;color:var(--ink)}
.page{position:absolute;left:0;top:0;width:960px;height:1064px;transform:scale(1.128125);transform-origin:0 0;overflow:hidden}
.abs{position:absolute}

/* header band */
.hero-band{left:0;top:0;width:960px;height:490px;
  background:linear-gradient(180deg,var(--sky-1) 0%,var(--sky-1) 15%,var(--sky-2) 55%,var(--sky-3) 100%)}
.hero-strip{left:0;top:442px;width:960px;height:48px;background:linear-gradient(180deg,rgba(60,110,140,.55),rgba(80,130,160,.55))}

.brand{left:26px;top:36px;font-size:58px;font-weight:700;color:var(--blue-deep);letter-spacing:-1px;line-height:1.15}
.translate{left:880px;top:20px;font-size:10px;color:#111;display:flex;align-items:center;gap:5px}
.flag{width:16px;height:11px;background:linear-gradient(180deg,#c9d6e8,#7f9cc6);border:1px solid #6b7fa0}
.cta{left:808px;top:40px;display:flex;align-items:center;gap:4px}
.cta-figure{width:40px;height:44px;border-radius:50%;background:radial-gradient(circle at 50% 40%,#4a9fd8,#1a5f96)}
.cta-label{font-size:15px;color:var(--blue)}

/* navigation */
.main-nav{left:153px;top:137px;width:654px;height:37px;border-radius:4px;display:flex;
  background:linear-gradient(180deg,#3d3d3d 0%,var(--nav-dark) 50%,#000 100%);box-shadow:0 4px 6px rgba(0,0,0,.25)}
.main-nav a{color:#eaeaea;text-decoration:none;font-size:14px;display:flex;align-items:center;justify-content:center;border-left:1px solid #555;height:100%}
.main-nav a:first-child{border-left:0;border-radius:4px 0 0 4px;background:linear-gradient(180deg,#4e93d6,#1a5fb0);color:var(--white)}

/* intro */
.intro-title{left:60px;top:266px;font-size:29px;font-weight:700;color:var(--blue-deep);letter-spacing:-.5px;line-height:36px}
.intro-title span{color:var(--grey-text)}
.intro-text{left:60px;top:306px;width:482px;font-size:11px;line-height:18.5px;color:#111}
.view-more{left:440px;top:361px;width:100px;text-align:right;font-size:12px;color:var(--red)}

.download-btn{left:63px;top:442px;width:207px;height:46px;border-radius:8px;
  background:linear-gradient(180deg,#6fb4ec,#1a64b6 55%,#0f4d92);box-shadow:0 2px 3px rgba(0,0,0,.3);
  color:var(--white);font-size:17px;font-weight:700;padding:14px 0 0 17px;letter-spacing:.3px}
.free-tag{left:190px;top:435px;width:42px;height:32px;background:#0f3f77;color:var(--white);font-size:8px;font-weight:700;text-align:center;padding-top:17px}
.pdf-sheet{left:233px;top:442px;width:35px;height:43px;background:linear-gradient(180deg,#fff,#e8e8e8);border:1px solid #aaa}
.download-note{left:279px;top:451px;width:285px;font-size:12px;line-height:16px;color:var(--white)}
.download-note b{color:var(--blue-deep);font-weight:700}

.video-frame{left:564px;top:199px;width:353px;height:270px;background:linear-gradient(135deg,#e8e6e2 0%,#b7b3ad 45%,#5e5b58 100%)}
.video-play{left:700px;top:296px}
.video-controls{left:564px;top:470px;width:353px;height:23px;background:linear-gradient(180deg,#e4e4e4,#a9a9a9);border-top:1px solid #fff}

/* content */
.content-band{left:0;top:490px;width:960px;height:60px;background:linear-gradient(180deg,#ececec,#fff)}
.section-title{left:17px;top:546px;font-size:20px;font-weight:700;color:var(--blue);line-height:24px}
.divider-v{left:698px;top:552px;width:1px;height:388px;background:var(--line)}
.section-text{left:20px;top:594px;width:666px;font-size:11px;line-height:20px;color:#222;text-align:justify}

.mail-table{left:12px;top:738px;width:687px;border-collapse:collapse;font-size:12px;position:absolute;table-layout:fixed}
.mail-table th{background:var(--blue-bar);color:var(--white);font-weight:700;text-align:left;padding:0 0 0 20px;height:33px}
.mail-table td{border:1px solid var(--line);padding:0 0 0 13px;height:33px;color:#222;vertical-align:middle;white-space:nowrap}
.mail-table tr.first td{height:40px;vertical-align:bottom;padding-bottom:6px}
.mail-table td:first-child{padding-left:23px}

/* sidebar */
.survey-icon{left:722px;top:553px;width:60px;height:62px;border-radius:4px;background:linear-gradient(135deg,#8fc3ec,#1d5fad)}
.side-title{font-size:15px;font-weight:700;color:var(--blue);line-height:18px}
.survey-form{left:739px;top:623px;width:115px}
.survey-row{display:flex;justify-content:space-between;align-items:center;height:30px;font-size:12px;color:#222}
.check{width:21px;height:21px;border:1px solid #bbb;background:linear-gradient(180deg,#fff,#e2e2e2)}
.submit-btn{left:744px;top:756px;width:92px;height:25px;background:linear-gradient(180deg,#5aa3e6,#1e64b5);color:var(--white);font-size:12px;text-align:center;line-height:25px}
.divider-h{left:716px;top:795px;width:205px;height:1px;background:var(--line)}
.promo-icon{left:720px;top:802px;width:62px;height:60px;border-radius:4px;background:linear-gradient(135deg,#f2f2f2,#b8bfc7)}
.promo-text{left:722px;top:874px;width:205px;font-size:12px;line-height:14px;color:#111}
.read-more{left:821px;top:902px;width:100px;text-align:right;font-size:12px;color:var(--red)}
.pager{top:918px;font-size:13px;color:var(--blue)}

/* footer */
.site-footer{left:0;top:970px;width:960px;height:94px;background:var(--blue-bar);color:var(--white)}
.footer-nav{left:19px;top:994px;display:flex;font-size:11px}
.footer-nav a{color:var(--white);text-decoration:none}
.copyright{left:19px;top:1024px;font-size:11px;color:var(--white)}
.connect{left:839px;top:994px;width:100px;text-align:right;font-size:11px;color:var(--white)}
.social{top:1013px;width:35px;height:35px;border-radius:5px;border:2px solid #cfe3f5}
</style>
</head>
<body>
<div class="page">
  <div class="abs hero-band"></div>
  <div class="abs hero-strip"></div>

  <div class="abs brand">lettrova.example</div>
  <div class="abs translate">Translate <span class="flag"></span></div>
  <div class="abs cta"><div class="cta-figure" role="img" aria-label="Support agent with headset"></div><span class="cta-label">Call to action</span></div>

  <nav class="abs main-nav">
    <a href="#" style="width:92px">Home</a>
    <a href="#" style="width:98px">About Us</a>
    <a href="#" style="width:100px">Services</a>
    <a href="#" style="width:93px">Pricing</a>
    <a href="#" style="width:81px">FAQ</a>
    <a href="#" style="width:100px">Contact Us</a>
    <a href="#" style="width:90px">Log In</a>
  </nav>

  <h1 class="abs intro-title">Lorem<span>Ipsum</span></h1>
  <p class="abs intro-text">Lorem Ipsum has been the industry's standard dummy text ever since the 1500s, when an unknown printer took a galley of type and scrambled it to make a type specimen book. It has survived not only five centuries, but also the leap into electronic typesetting.</p>
  <a class="abs view-more">View more</a>

  <div class="abs download-btn">DOWNLOAD</div>
  <div class="abs free-tag">FREE</div>
  <div class="abs pdf-sheet"></div>
  <p class="abs download-note">Click here to download the <b>Terms and Conditions</b> as PDF file</p>

  <div class="abs video-frame" role="img" aria-label="Video still: a hand resting on a computer mouse beside a laptop keyboard"></div>
  <svg class="abs video-play" width="80" height="84" viewBox="0 0 80 84" aria-hidden="true"><path d="M2 2 L76 42 L2 82 Z" fill="rgba(255,255,255,.5)"/></svg>
  <svg class="abs video-controls" width="353" height="23" viewBox="0 0 353 23" aria-hidden="true">
    <path d="M8 6 L18 11.5 L8 17 Z" fill="#222"/>
    <line x1="25" y1="2" x2="25" y2="21" stroke="#888"/>
    <circle cx="35" cy="11.5" r="5" fill="#ddd" stroke="#555"/>
    <rect x="42" y="9" width="168" height="5" rx="2" fill="#eee" stroke="#777"/>
    <text x="225" y="15" font-size="8" fill="#222" font-family="Arimo, sans-serif">0:00 / 0:00</text>
    <line x1="270" y1="2" x2="270" y2="21" stroke="#888"/>
    <path d="M277 9 h4 l4 -3 v11 l-4 -3 h-4 z" fill="#333"/>
    <line x1="296" y1="2" x2="296" y2="21" stroke="#888"/>
    <rect x="302" y="6" width="16" height="11" fill="#333"/>
    <line x1="324" y1="2" x2="324" y2="21" stroke="#888"/>
    <path d="M331 15 L338 8 L345 15 Z" fill="#333"/>
  </svg>

  <div class="abs content-band"></div>
  <h2 class="abs section-title">Contrary to popular</h2>
  <div class="abs divider-v"></div>
  <p class="abs section-text">It has roots in a piece of classical Latin literature from 45 BC, making it over 2000 years old. Aldous Penbright, a Latin professor at Marlowe Ridge College in Virginia, looked up one of the more obscure Latin words, consectetur, from a Lorem Ipsum passage, and going through the cites of the word in classical literature, discovered the undoubtable source. Lorem Ipsum comes from sections 1.10.32 and 1.10.33 of "de Finibus Bonorum et Malorum" (The Extremes of Good and Evil) by Varenus, written in 45 BC.This book is a treatise on the theory of ethics, very popular during the Renaissance. The first line of Lorem Ipsum, "Lorem ipsum dolor sit amet..", comes from a line in section 1.10.32.</p>

  <table class="mail-table">
    <colgroup><col style="width:114px"><col style="width:131px"><col style="width:144px"><col style="width:137px"><col style="width:161px"></colgroup>
    <thead><tr><th>Data Recd</th><th>Document Type</th><th>Scan/Not Scan</th><th>Document Name</th><th>Sender</th></tr></thead>
    <tbody>
      <tr class="first"><td>Date Recd</td><td>Document Type</td><td>Scanned/Not Scan</td><td>Document Name</td><td>Supplier Name</td></tr>
      <tr><td>25 Feb 2011</td><td>Invoice</td><td>Scanned</td><td></td><td>Torvale - Gas</td></tr>
      <tr><td></td><td>‘Restricted’</td><td>Client Request</td><td></td><td>Letter fm Aunty Joan</td></tr>
      <tr><td></td><td>Prospectus</td><td>Too large/ Not</td><td></td><td>Dralmere</td></tr>
      <tr><td></td><td></td><td>Scanned</td><td></td><td></td></tr>
    </tbody>
  </table>

  <div class="abs survey-icon" role="img" aria-label="Computer monitor with a globe"></div>
  <h3 class="abs side-title" style="left:796px;top:573px">Online Surveys</h3>
  <form class="abs survey-form">
    <div class="survey-row">Excellent :<span class="check"></span></div>
    <div class="survey-row">Good:<span class="check"></span></div>
    <div class="survey-row">Fari:<span class="check"></span></div>
    <div class="survey-row">Poor:<span class="check"></span></div>
  </form>
  <div class="abs submit-btn">Submit</div>
  <div class="abs divider-h"></div>
  <div class="abs promo-icon" role="img" aria-label="Airmail envelope with a pen"></div>
  <h3 class="abs side-title" style="left:796px;top:823px">Promotional copy</h3>
  <p class="abs promo-text">Lorem Ipsum is simply dummy text of the printing and typesetting industry.</p>
  <a class="abs read-more">read more</a>
  <span class="abs pager" style="left:718px">«</span>
  <span class="abs pager" style="left:917px">»</span>

  <footer class="abs site-footer"></footer>
  <nav class="abs footer-nav">
    <a href="#" style="width:66px">Home</a>
    <a href="#" style="width:79px">About Us</a>
    <a href="#" style="width:79px">Services</a>
    <a href="#" style="width:70px">Pricing</a>
    <a href="#" style="width:59px">FAQ</a>
    <a href="#" style="width:91px">Contact Us</a>
    <a href="#">Log In</a>
  </nav>
  <p class="abs copyright">© All Copyrights.lettrova.reserved</p>
  <p class="abs connect">Conntect Us</p>
  <span class="abs social" style="left:828px;background:#3b6fb6" role="img" aria-label="Social network link"></span>
  <span class="abs social" style="left:867px;background:#5fb3e3" role="img" aria-label="Social network link"></span>
  <span class="abs social" style="left:907px;background:#f29a1e" role="img" aria-label="News feed link"></span>
</div>
</body>
</html>
```